Harbor Ridge Chapel
Every Man, Woman, and Child
Modern
Mark Fenwick
lead Pastor
4527 Delford
Linden Bay, Ca 90417
mark.fenwick@harborridgechapel.example
harborridgechapel.example
front of the card is the logo, and all the info on the back
use the logo, and try harbor ridge chapel behind the logo and try it under the logo.

```html
<!DOCTYPE html>
<html lang="en">
<head>
<meta charset="utf-8">
<title>Harbor Ridge Chapel — Business Card</title>
<link rel="stylesheet" href="https://fonts.googleapis.com/css2?family=Montserrat:wght@400;600&family=Open+Sans:wght@400;600&display=swap">
<style>
  :root {
    --bg: #d9d9d9;
    --card: #141414;
    --blue: #3f74c4;
    --white: #ffffff;
    --grey: #a9a9a9;
  }
  * { box-sizing: border-box; margin: 0; padding: 0; }
  html, body {
    width: 1200px;
    height: 901px;
    overflow: hidden;
    background: var(--bg);
  }
  .canvas {
    width: 1200px;
    height: 901px;
    display: flex;
    flex-direction: column;
    align-items: center;
    justify-content: center;
    gap: 48px;
  }
  .card {
    position: relative;
    width: 660px;
    height: 377px;
    background: var(--card);
    border-radius: 22px;
    overflow: hidden;
    color: var(--white);
    font-family: "Open Sans", sans-serif;
  }
  .card__band {
    position: absolute;
    left: 0; right: 0; bottom: 0;
    height: 14px;
    background: var(--blue);
  }

  /* Front */
  .brand {
    position: absolute;
    top: 104px;
    left: 0; right: 0;
    display: flex;
    flex-direction: column;
    align-items: center;
  }
  .brand__dot {
    width: 54px;
    height: 54px;
    border-radius: 50%;
    background: var(--blue);
    margin-bottom: 18px;
  }
  .brand__name {
    font-family: "Montserrat", sans-serif;
    font-weight: 600;
    font-size: 34px;
    line-height: 1.1;
    letter-spacing: 1px;
    text-transform: uppercase;
    color: var(--white);
  }
  .brand__sub {
    font-family: "Montserrat", sans-serif;
    font-weight: 400;
    font-size: 20px;
    line-height: 1.2;
    letter-spacing: 5px;
    text-transform: uppercase;
    color: var(--white);
  }
  .front__web {
    position: absolute;
    right: 40px;
    bottom: 32px;
    font-size: 15px;
    color: var(--grey);
  }

  /* Back */
  .contact {
    position: absolute;
    left: 52px;
    top: 56px;
  }
  .contact__name {
    display: flex;
    align-items: center;
    gap: 12px;
    font-family: "Montserrat", sans-serif;
    font-weight: 600;
    font-size: 22px;
    letter-spacing: 1px;
    text-transform: uppercase;
  }
  .contact__marker {
    width: 12px;
    height: 28px;
    background: var(--blue);
  }
  .contact__surname { color: var(--blue); }
  .contact__role {
    margin: 4px 0 0 24px;
    font-size: 15px;
    color: var(--grey);
  }
  .contact__details {
    margin: 54px 0 0 24px;
    font-size: 15px;
    line-height: 1.55;
    color: var(--white);
    list-style: none;
  }
  .contact__label {
    display: inline-block;
    width: 58px;
    color: var(--blue);
  }
</style>
</head>
<body>
<main class="canvas">

  <section class="card card--front" aria-label="Card front">
    <div class="brand">
      <span class="brand__dot"></span>
      <span class="brand__name">Harbor Ridge</span>
      <span class="brand__sub">Chapel</span>
    </div>
    <p class="front__web">harborridgechapel.example</p>
    <div class="card__band"></div>
  </section>

  <section class="card card--back" aria-label="Card back">
    <div class="contact">
      <h1 class="contact__name">
        <span class="contact__marker"></span>
        <span>Mark <span class="contact__surname">Fenwick</span></span>
      </h1>
      <p class="contact__role">lead Pastor</p>
      <ul class="contact__details">
        <li>4527 Delford</li>
        <li>Linden Bay, Ca 90417</li>
        <li><span class="contact__label">Phone:</span>949 555-0142</li>
        <li><span class="contact__label">Email:</span>mark.fenwick@harborridgechapel.example</li>
        <li><span class="contact__label">Web:</span>harborridgechapel.example</li>
      </ul>
    </div>
    <div class="card__band"></div>
  </section>

</main>
</body>
</html>
```